Vessa Almond Protein - Less, but better

Design a protein powder pouch (350g). Take inspiration from Brimora.co and put the same information on the pouch and add "made in Australia". I do not want it to be exactly the same design but just take some inspiration from it.

```html
<!DOCTYPE html>
<html lang="en">
<head>
<meta charset="utf-8">
<title>Vessa Premium Protein – Pouch Front</title>
<link href="https://fonts.googleapis.com/css2?family=Bebas+Neue&family=Hind:wght@400;500&family=Roboto+Condensed:wght@300;400&display=swap" rel="stylesheet">
<style>
  :root {
    --stage: #ececec;
    --forest: #0f5330;
    --tangerine: #dc6f37;
    --cream: #f3e5d2;
    --marigold: #f9bc5a;
    --white: #ffffff;
    --ink: #3a3a3a;
    --icon-line: #fff4e0;
  }
  html, body {
    margin: 0;
    width: 1200px;
    height: 800px;
    overflow: hidden;
    background: var(--stage);
  }
  .stage {
    position: relative;
    width: 1200px;
    height: 800px;
  }
  .pouch-front {
    position: absolute;
    left: 358px;
    top: 40px;
    width: 484px;
    height: 720px;
    display: block;
  }
  .brand-name {
    font-family: "Hind", sans-serif;
    font-weight: 500;
    fill: var(--white);
  }
  .tagline {
    font-family: "Hind", sans-serif;
    font-weight: 400;
    fill: var(--white);
    letter-spacing: 2px;
  }
  .eyebrow {
    font-family: "Roboto Condensed", sans-serif;
    font-weight: 400;
    fill: var(--white);
  }
  .product-title {
    font-family: "Bebas Neue", sans-serif;
    fill: var(--white);
  }
  .flavour-pill { fill: var(--white); }
  .flavour-name {
    font-family: "Roboto Condensed", sans-serif;
    font-weight: 400;
    fill: var(--ink);
  }
  .benefit {
    font-family: "Hind", sans-serif;
    font-weight: 400;
    fill: var(--white);
  }
  .badge-ring {
    fill: rgba(255, 244, 224, 0.12);
    stroke: var(--icon-line);
    stroke-width: 2.5;
  }
  .badge-label, .origin {
    font-family: "Roboto Condensed", sans-serif;
    font-weight: 400;
    fill: var(--white);
  }
</style>
</head>
<body>
<main class="stage">
  <svg class="pouch-front" viewBox="0 0 932 1386" xmlns="http://www.w3.org/2000/svg" aria-label="Vessa Premium Protein pouch front">
    <defs>
      <linearGradient id="panel-tones" x1="0" y1="0" x2="0.35" y2="1">
        <stop offset="0" stop-color="#0f5330"/>
        <stop offset="0.36" stop-color="#0f5330"/>
        <stop offset="0.5" stop-color="#dc6f37"/>
        <stop offset="0.74" stop-color="#dc6f37"/>
        <stop offset="0.9" stop-color="#eaa050"/>
        <stop offset="1" stop-color="#f3c777"/>
      </linearGradient>
    </defs>

    <rect x="0" y="0" width="932" height="1386" fill="url(#panel-tones)" role="img" aria-label="Colour-block background artwork in green, orange, cream and yellow"/>

    <text class="brand-name" x="466" y="400" font-size="150" text-anchor="middle">Vessa</text>
    <text class="tagline" x="466" y="470" font-size="38" text-anchor="middle">less, but better</text>

    <text class="eyebrow" x="82" y="662" font-size="22">DAILY NOURISHING</text>
    <text class="product-title" x="76" y="740" font-size="90" textLength="484" lengthAdjust="spacingAndGlyphs">PREMIUM PROTEIN</text>

    <rect class="flavour-pill" x="74" y="760" width="308" height="70" rx="14"/>
    <text class="flavour-name" x="117" y="807" font-size="32">VANILLA BEAN</text>

    <text class="benefit" x="86" y="895" font-size="28">- 25g Protein per serve</text>
    <text class="benefit" x="86" y="943" font-size="28">- Low Sugar &amp; Low Carb</text>
    <text class="benefit" x="86" y="990" font-size="28">- No Artificial Flavours</text>
    <text class="benefit" x="86" y="1038" font-size="28">- Digestive Enzyme Blend</text>

    <g role="img" aria-label="Muscle icon">
      <circle class="badge-ring" cx="352" cy="1230" r="36"/>
    </g>
    <g role="img" aria-label="Recovery icon">
      <circle class="badge-ring" cx="462" cy="1230" r="36"/>
    </g>
    <g role="img" aria-label="Gut friendly icon">
      <circle class="badge-ring" cx="576" cy="1230" r="36"/>
    </g>
    <text class="badge-label" x="352" y="1294" font-size="17" text-anchor="middle">MUSCLE</text>
    <text class="badge-label" x="462" y="1295" font-size="17" text-anchor="middle">RECOVERY</text>
    <text class="badge-label" x="581" y="1295" font-size="17" text-anchor="middle">GUT FRIENDLY</text>

    <text class="origin" x="467" y="1351" font-size="20" text-anchor="middle">MADE IN AUSTRALIA</text>
  </svg>
</main>
</body>
</html>
```